Weight Loss Banner Ad

We need banner ads for our website, www.bluvantaplan.com. We would like to see Banner ads that represent what you think is the most captivating aspect of The Bluvanta Plan. Please review the website.

The banner ad should be something you REALLY want to click on. It needs to include the name and/or logo and the slogan "Gourmet Meals Direct To Your House"

We will want the final ad in multiple sizes but it should use the same image and copy.

Logo is attached, so are images. Feel free to use your own if you think you have a better on

Size (pixels):
468 x 60
392 x 72
234 x 60
125 x 125
120 x 90
120 x 60
88 x 31
120 x 240
120 x 600
160 x 600

Target Market(s)

Fitness Enthusiast looking to lose weight.

Industry/Entity Type

Weight

Font styles to use
Sans Serif

Requirements
Must have
• See Description
Nice to have
• Should be awesome and make you want to buy some food. Also you may want to say something about the price:

i.e. Starting at only $99

```html
<!DOCTYPE html>
<html lang="en">
<head>
<meta charset="utf-8">
<title>The Bluvanta Plan – Banner Set</title>
<link rel="stylesheet" href="https://fonts.googleapis.com/css2?family=Open+Sans:wght@400;700&family=Tinos&display=swap">
<style>
  :root {
    --canvas: #ffffff;
    --panel: #f3f3f3;
    --panel-line: #c9c9c9;
    --header-grey: #8a8a8a;
    --lime: #8cc63f;
    --ink: #555555;
    --ink-soft: #6b6b6b;
    --ink-dark: #222222;
    --gold-top: #ffe27a;
    --gold-bottom: #f2a900;
    --button-edge: #7a6a3a;
    --food-green: #7fb24a;
    --food-orange: #e08a3c;
    --food-red: #8a2f4a;
  }
  * { box-sizing: border-box; margin: 0; padding: 0; }
  html, body { width: 923px; height: 1200px; overflow: hidden; background: var(--canvas); }
  body { position: relative; font-family: "Open Sans", Arial, sans-serif; }

  .banner { position: absolute; background: var(--panel); border: 1px solid var(--panel-line); overflow: hidden; }
  .banner > * { position: absolute; }
  .header-shape { left: 0; top: 0; }
  .brand { color: var(--lime); font-weight: 700; line-height: 1.05; }
  .headline { font-weight: 700; line-height: 1; white-space: nowrap; letter-spacing: -0.5px; }
  .headline--lime { color: var(--lime); }
  .headline--grey { color: var(--ink); }
  .food-photo {
    background: linear-gradient(120deg, var(--food-green) 0%, #b9d77a 30%, var(--food-orange) 55%, var(--food-red) 75%, #d9c9a8 100%);
  }
  .slogan { color: var(--ink-soft); line-height: 1; white-space: nowrap; }
  .slogan--boxed { border: 2px solid var(--ink-soft); background: #fff; display: flex; align-items: center; justify-content: center; }
  .price-lead { color: var(--ink-dark); line-height: 1; white-space: nowrap; }
  .price-badge { border-radius: 50%; background: var(--lime); color: var(--ink-dark); display: flex; align-items: center; justify-content: center; font-weight: 400; line-height: 1; }
  .price-badge sup { font-size: 0.5em; align-self: flex-start; margin-top: 0.35em; }
  .order-button {
    background: linear-gradient(var(--gold-top), var(--gold-bottom));
    border: 2px solid var(--button-edge); border-radius: 3px;
    box-shadow: 0 3px 4px rgba(0,0,0,0.35);
    font-family: "Tinos", "Times New Roman", serif; color: var(--ink-dark);
    display: flex; align-items: center; justify-content: center;
  }
  .site-url { color: var(--ink-dark); line-height: 1; white-space: nowrap; }

  /* Skyscraper */
  .banner--tall { left: 28px; top: 46px; width: 299px; height: 1113px; }
  .banner--tall .brand { left: 20px; width: 259px; text-align: center; top: 48px; font-size: 36px; }
  .banner--tall .headline { left: 0; width: 299px; text-align: center; font-size: 42px; }
  .banner--tall .food-photo { left: 0; top: 406px; width: 299px; height: 305px; border-radius: 0 0 0 40px; }
  .banner--tall .slogan { left: 10px; width: 240px; text-align: center; font-size: 30px; line-height: 41px; top: 774px; white-space: normal; }
  .banner--tall .price-lead { left: 28px; top: 920px; font-size: 24px; }
  .banner--tall .price-badge { left: 212px; top: 886px; width: 82px; height: 82px; font-size: 44px; }
  .banner--tall .order-button { left: 13px; top: 972px; width: 269px; height: 68px; font-size: 36px; }
  .banner--tall .footer-band { left: 0; top: 1052px; width: 299px; height: 61px; background: var(--lime); display: flex; align-items: center; justify-content: center; }
  .banner--tall .site-url { font-size: 26px; font-weight: 700; }

  /* Medium rectangle */
  .banner--wide { left: 351px; top: 166px; width: 550px; height: 462px; }
  .banner--wide .brand { left: 24px; top: 20px; width: 205px; font-size: 28px; }
  .banner--wide .headline { left: 26px; font-size: 58px; }
  .banner--wide .slogan--boxed { left: 28px; top: 314px; width: 492px; height: 40px; font-size: 27px; }
  .banner--wide .price-lead { left: 22px; top: 420px; font-size: 24px; }
  .banner--wide .price-badge { left: 209px; top: 374px; width: 78px; height: 78px; font-size: 42px; }
  .banner--wide .order-button { left: 290px; top: 366px; width: 230px; height: 58px; font-size: 32px; }
  .banner--wide .site-url { right: 28px; top: 434px; font-size: 20px; }

  /* Small rectangle */
  .banner--small { left: 421px; top: 674px; width: 419px; height: 347px; }
  .banner--small .brand { left: 18px; top: 16px; width: 160px; font-size: 21px; }
  .banner--small .headline { left: 20px; font-size: 44px; }
  .banner--small .slogan--boxed { left: 22px; top: 234px; width: 373px; height: 34px; font-size: 21px; }
  .banner--small .price-lead { left: 18px; top: 307px; font-size: 17px; }
  .banner--small .price-badge { left: 154px; top: 280px; width: 58px; height: 58px; font-size: 32px; }
  .banner--small .order-button { left: 216px; top: 277px; width: 179px; height: 44px; font-size: 25px; }
  .banner--small .site-url { right: 24px; top: 327px; font-size: 14px; }
</style>
</head>
<body>

<section class="banner banner--tall">
  <svg class="header-shape" width="299" height="235" viewBox="0 0 299 235">
    <rect x="0" y="0" width="299" height="180" fill="var(--header-grey)"/>
    <path d="M0 180 H299 V194 H203 L152 231 L138 194 H0 Z" fill="var(--lime)"/>
  </svg>
  <p class="brand">The Bluvanta Plan</p>
  <h1 class="headline headline--lime" style="top:250px">EFFORTLESS</h1>
  <p class="headline headline--grey" style="top:311px">WEIGHT</p>
  <p class="headline headline--grey" style="top:367px">LOSS</p>
  <div class="food-photo" role="img" aria-label="Plate of grilled vegetables with lettuce leaves"></div>
  <p class="slogan">Gourmet Meals Direct To Your House</p>
  <p class="price-lead">Starting at only</p>
  <div class="price-badge"><sup>$</sup>99</div>
  <div class="order-button">Order Now</div>
  <div class="footer-band"><span class="site-url">bluvantaplan.com</span></div>
</section>

<section class="banner banner--wide">
  <div class="food-photo" style="left:0;top:0;width:550px;height:215px;clip-path:polygon(44% 0,100% 0,100% 100%,72% 100%,44% 48%)" role="img" aria-label="Grilled vegetables on a white plate"></div>
  <svg class="header-shape" width="550" height="142" viewBox="0 0 550 142">
    <path d="M0 0 H242 L242 102 H0 Z" fill="var(--header-grey)"/>
    <path d="M0 102 H258 L278 114 H130 L100 140 L88 114 H0 Z" fill="var(--lime)"/>
  </svg>
  <p class="brand">The Bluvanta Plan</p>
  <h2 class="headline headline--lime" style="top:183px">EFFORTLESS</h2>
  <p class="headline headline--grey" style="top:245px">WEIGHT LOSS</p>
  <p class="slogan slogan--boxed">Gourmet Meals Direct To Your House</p>
  <p class="price-lead">Starting at only</p>
  <div class="price-badge"><sup>$</sup>99</div>
  <div class="order-button">Order Now</div>
  <p class="site-url">bluvantaplan.com</p>
</section>

<section class="banner banner--small">
  <div class="food-photo" style="left:0;top:0;width:419px;height:165px;clip-path:polygon(44% 0,100% 0,100% 100%,72% 100%,44% 50%)" role="img" aria-label="Grilled vegetables on a white plate"></div>
  <svg class="header-shape" width="419" height="112" viewBox="0 0 419 112">
    <path d="M0 0 H184 L184 83 H0 Z" fill="var(--header-grey)"/>
    <path d="M0 83 H196 L212 92 H100 L76 111 L66 92 H0 Z" fill="var(--lime)"/>
  </svg>
  <p class="brand">The Bluvanta Plan</p>
  <h2 class="headline headline--lime" style="top:135px">EFFORTLESS</h2>
  <p class="headline headline--grey" style="top:176px">WEIGHT LOSS</p>
  <p class="slogan slogan--boxed">Gourmet Meals Direct To Your House</p>
  <p class="price-lead">Starting at only</p>
  <div class="price-badge"><sup>$</sup>99</div>
  <div class="order-button">Order Now</div>
  <p class="site-url">bluvantaplan.com</p>
</section>

</body>
</html>
```